Premium Organic Ceremonial Matcha Green Tea - Product Label

Two Label Bag Sizes: 18x30cm and 17x24cm

Be EXTRA Creative.. please message me with any questions and I will respond quickly.

Target Market(s)

Health, Organic, Green Tea Matcha Drinkers

Industry/Entity Type

Product

Requirements
Must have
• Organic Matcha Green Tea
• Try to incorporate geometry in logo into design... not mandatory but preferred for branding.

```html
<!DOCTYPE html>
<html lang="en">
<head>
<meta charset="utf-8">
<title>Verdant Crest – Premium Ceremonial Organic Matcha Label</title>
<link rel="stylesheet" href="https://fonts.googleapis.com/css2?family=Oswald:wght@400;500;600&family=Playball&family=Rajdhani:wght@500;600&display=swap">
<style>
  :root {
    --backdrop: #4a4a4a;
    --label-white: #f7f8f6;
    --label-grey: #e3e5e2;
    --hex-tint: #eceeeb;
    --leaf-green: #3f8f2f;
    --leaf-green-dark: #2d6e22;
    --leaf-green-light: #6aac43;
    --gold: #e0a21c;
    --gold-light: #f5d25a;
    --ink: #262626;
    --bar-black: #1d1d1d;
    --matcha: #a9cb5e;
    --matcha-deep: #8fb648;
  }
  html, body {
    margin: 0;
    padding: 0;
    width: 1071px;
    height: 1200px;
    overflow: hidden;
    background: var(--backdrop);
  }
  .canvas { display: block; width: 1071px; height: 1200px; }
  .brand-name { font-family: "Oswald", sans-serif; font-weight: 500; fill: #ffffff; }
  .tagline { font-family: "Playball", cursive; fill: #ffffff; }
  .subtitle { font-family: "Playball", cursive; fill: var(--leaf-green-dark); }
  .product-title { font-family: "Oswald", sans-serif; font-weight: 600; fill: var(--leaf-green); }
  .product-kind { font-family: "Rajdhani", sans-serif; font-weight: 500; fill: var(--leaf-green); }
  .uses { font-family: "Rajdhani", sans-serif; font-weight: 600; fill: var(--ink); }
  .benefits { font-family: "Rajdhani", sans-serif; font-weight: 500; fill: #ffffff; letter-spacing: 0.5px; }
  .pack-info { font-family: "Rajdhani", sans-serif; font-weight: 600; fill: var(--ink); }
</style>
</head>
<body>
<svg class="canvas" width="1071" height="1200" viewBox="0 0 1071 1200" xmlns="http://www.w3.org/2000/svg">
  <defs>
    <linearGradient id="labelBase" x1="0" y1="0" x2="1" y2="0">
      <stop offset="0" stop-color="var(--label-grey)"/>
      <stop offset="0.5" stop-color="var(--label-white)"/>
      <stop offset="1" stop-color="var(--label-grey)"/>
    </linearGradient>
    <linearGradient id="greenPanel" x1="0" y1="0" x2="0" y2="1">
      <stop offset="0" stop-color="var(--leaf-green-light)"/>
      <stop offset="1" stop-color="var(--leaf-green)"/>
    </linearGradient>
    <linearGradient id="goldEdge" x1="0" y1="0" x2="1" y2="1">
      <stop offset="0" stop-color="var(--gold-light)"/>
      <stop offset="1" stop-color="var(--gold)"/>
    </linearGradient>
    <linearGradient id="vineFade" x1="0" y1="0" x2="0" y2="1">
      <stop offset="0" stop-color="var(--leaf-green-light)" stop-opacity="0.5"/>
      <stop offset="1" stop-color="var(--leaf-green-light)" stop-opacity="0"/>
    </linearGradient>
    <linearGradient id="powderArea" x1="0" y1="0" x2="0" y2="1">
      <stop offset="0" stop-color="var(--matcha)"/>
      <stop offset="1" stop-color="var(--matcha-deep)"/>
    </linearGradient>
  </defs>

  <!-- label base -->
  <rect class="label-base" x="198" y="98" width="704" height="1022" fill="url(#labelBase)"/>

  <!-- faint hexagon background area -->
  <rect role="img" aria-label="Faint hexagon background pattern" x="230" y="300" width="640" height="560" fill="var(--hex-tint)" opacity="0.6"/>

  <!-- hanging vine areas -->
  <rect role="img" aria-label="Hanging green vine illustration" x="200" y="98" width="140" height="200" fill="url(#vineFade)"/>
  <rect role="img" aria-label="Hanging green vine illustration" x="768" y="98" width="132" height="200" fill="url(#vineFade)"/>

  <!-- brand panel -->
  <path class="brand-panel-edge" d="M340 98 L340 306 L442 492 L674 492 L768 306 L768 98 Z" fill="url(#goldEdge)"/>
  <path class="brand-panel" d="M347 98 L347 304 L446 486 L670 486 L761 304 L761 98 Z" fill="url(#greenPanel)"/>

  <!-- brand name -->
  <circle cx="446" cy="360" r="8" fill="#ffffff"/>
  <text class="brand-name" x="572" y="374" font-size="34" text-anchor="middle">Verdant Crest</text>

  <!-- tagline -->
  <g class="tagline" font-size="17">
    <path d="M436 393 l4 5 l9 -11" stroke="#fff" stroke-width="2" fill="none"/>
    <text x="452" y="399">Pure</text>
    <path d="M516 393 l4 5 l9 -11" stroke="#fff" stroke-width="2" fill="none"/>
    <text x="532" y="399">Organic</text>
    <path d="M610 393 l4 5 l9 -11" stroke="#fff" stroke-width="2" fill="none"/>
    <text x="626" y="399">Natural</text>
  </g>

  <!-- titles -->
  <text class="subtitle" x="562" y="568" font-size="34" text-anchor="middle">Premium Ceremonial</text>
  <text class="product-title" x="559" y="662" font-size="84" text-anchor="middle" textLength="534" lengthAdjust="spacingAndGlyphs">ORGANIC MATCHA</text>
  <line x1="316" y1="678" x2="800" y2="678" stroke="var(--leaf-green)" stroke-width="2"/>
  <text class="product-kind" x="568" y="730" font-size="54" text-anchor="middle" textLength="244" lengthAdjust="spacingAndGlyphs">GREEN TEA</text>

  <!-- powder photo area -->
  <rect role="img" aria-label="Photo of a mound of green matcha powder" x="364" y="748" width="408" height="160" rx="8" fill="url(#powderArea)"/>

  <!-- bottom band -->
  <path class="bottom-band" d="M198 836 L328 884 L800 884 L902 836 L902 1120 L198 1120 Z" fill="var(--leaf-green)"/>
  <path class="bottom-window-edge" d="M198 830 L328 878 L800 878 L902 830 L902 838 L806 884 L806 1010 Q806 1116 566 1118 Q324 1116 324 1010 L324 884 L198 838 Z" fill="url(#goldEdge)"/>
  <path class="bottom-window" d="M330 908 L800 908 L800 1010 Q800 1110 566 1112 Q330 1110 330 1010 Z" fill="var(--label-white)"/>
  <rect x="330" y="884" width="470" height="26" fill="var(--label-white)"/>

  <!-- uses & benefits -->
  <text class="uses" x="556" y="950" font-size="40" text-anchor="middle" textLength="388" lengthAdjust="spacingAndGlyphs">BAKING•SMOOTHIES•LATTE</text>
  <rect class="benefits-bar" x="362" y="962" width="388" height="22" fill="var(--bar-black)"/>
  <text class="benefits" x="556" y="979" font-size="15" text-anchor="middle" textLength="370" lengthAdjust="spacingAndGlyphs">IMPROVE MEMORY AND HEALTH &#160;•&#160; ENHANCED FOCUS</text>

  <!-- badges -->
  <circle class="badge" cx="387" cy="1030" r="28" fill="#ffffff" stroke="var(--leaf-green-dark)" stroke-width="4"/>
  <circle class="badge" cx="722" cy="1036" r="27" fill="#ffffff" stroke="var(--leaf-green-dark)" stroke-width="4"/>

  <!-- pack info -->
  <text class="pack-info" x="548" y="1035" font-size="19" text-anchor="middle" textLength="218" lengthAdjust="spacingAndGlyphs">NET WEIGHT : 113 G ( 4 OZ )</text>
  <text class="pack-info" x="548" y="1059" font-size="19" text-anchor="middle" textLength="216" lengthAdjust="spacingAndGlyphs">PRODUCT OF COUNTRY NAME</text>
</svg>
</body>
</html>
```